The Marlow Wellness Studio (marlowstudio.example)

One page website (already purchased the theme) introducing the online clinic, with video, sections on the page our process, the technology, blog, the practitioner, contact, testimonials, find out more (see copy below) I am in the closing stages of having some collateral prepared I will load up the files that are in place so far so you get the feel for the brand and the current progress on the a brochure. The theme I have currently is loaded with demo data . this needs to be deleted and replaced. See here marlowstudio.example.

Target Market(s)

Female 30-50

Coding

Coded - Design and coding required

Number of Pages Required

1 page

Font styles to use
Serif
Sans Serif

Colors
33a6d7
3277b5

Requirements
Must have
• Consistent feel with existing A4 brochure, Trifold Brochure and business card,

Intro image & Outcome statement - Recharge Your Energy
Video & Free Access Offer
Why Energy
Our Process
About Vireq Technology
Getting Started
About Tobin
Our Services
Testimonials
Contact
Blog

Nice to have
• Suggestions for images.

```html
<!DOCTYPE html>
<html lang="en">
<head>
<meta charset="utf-8">
<title>The Marlow Wellness Studio</title>
<link rel="stylesheet" href="https://fonts.googleapis.com/css2?family=Roboto:wght@400;500;700&family=Montserrat:wght@400;500;600&display=swap">
<style>
:root{
  --sky:#33a6d7;
  --blue:#3277b5;
  --ink:#222;
  --text:#444;
  --muted:#777;
  --tile:#eeeeee;
  --foot:#222225;
  --foot-deep:#161618;
  --field:#2c2c30;
  --white:#fff;
  --star:#f5a623;
}
*{box-sizing:border-box;margin:0;padding:0}
html,body{width:1200px;height:4866px;overflow:hidden}
body{position:relative;font-family:"Montserrat",sans-serif;color:var(--text);background:var(--white)}
section,header,footer{position:absolute;left:0;width:1200px}
.abs{position:absolute}
h2{font-family:"Roboto",sans-serif;font-weight:500;font-size:38px;color:var(--ink);text-align:center;letter-spacing:-.5px}
h2 em{font-style:normal;color:var(--sky)}

/* header */
.site-header{top:0;height:110px;background:var(--white);border-bottom:1px solid #ddd}
.brand{position:absolute;left:62px;top:34px;display:flex;align-items:center;gap:12px}
.brand-dot{width:46px;height:46px;border-radius:50%;background:#d8d8d8}
.brand-name{font-family:"Roboto",sans-serif;font-weight:500;font-size:24px;color:var(--sky);line-height:1}
.phone{position:absolute;right:80px;top:18px;font-family:"Roboto",sans-serif;font-weight:500;font-size:17px;color:var(--blue);display:flex;align-items:center;gap:8px}
.nav{position:absolute;right:78px;top:64px;display:flex;gap:30px;font-family:"Roboto",sans-serif;font-size:16px;color:var(--ink)}

/* hero */
.hero{top:110px;height:574px;background:linear-gradient(180deg,#7f9fc0 0%,#a9bdd2 30%,#6b7f8e 55%,#4d5a3c 78%,#3b4a2a 100%)}
.hero-title{top:160px;width:100%;text-align:center;font-family:"Roboto",sans-serif;font-weight:500;font-size:52px;color:var(--white);letter-spacing:-1px}
.hero-sub{top:232px;width:100%;text-align:center;font-family:"Roboto",sans-serif;font-size:36px;line-height:44px;color:var(--white)}
.btn{display:inline-flex;align-items:center;justify-content:center;background:var(--sky);color:var(--white);font-family:"Roboto",sans-serif;font-size:18px;border-radius:24px;height:44px}
.hero-btns{top:354px;left:404px;display:flex;gap:20px}
.hero-btns .btn{width:182px}
.btn-play{gap:14px;padding-left:6px;justify-content:flex-start}
.btn-play span.ic{width:34px;height:34px;border-radius:50%;background:var(--white);display:flex;align-items:center;justify-content:center}

/* why */
.why{top:684px;height:352px}
.why .ring{border-radius:50%;background:#e6f3fa}
.why h2{position:absolute;top:124px;width:100%}
.why p{position:absolute;top:208px;left:210px;width:780px;text-align:center;font-size:17px;line-height:32px;color:#333}

/* process */
.process{top:1036px;height:640px;background:linear-gradient(180deg,#f2b24a 0%,#e58a2c 12%,#8d6a34 30%,#6b7a3a 60%,#4f6328 85%,#3c4d22 100%)}
.process h2{position:absolute;top:134px;width:100%;color:var(--white);font-size:36px}
.process .rule{top:190px;left:572px;width:56px;height:3px;background:var(--white)}
.step{position:absolute;width:382px;height:130px;background:var(--white);border-radius:65px;display:flex;align-items:center}
.step .txt{flex:1;padding-left:60px}
.step h3{font-family:"Roboto",sans-serif;font-weight:500;font-size:21px;color:var(--ink);margin-bottom:6px}
.step p{font-size:13px;line-height:18px;color:#333;width:200px}
.step .ic{width:98px;height:98px;border-radius:50%;background:linear-gradient(135deg,var(--sky),var(--blue));display:flex;align-items:center;justify-content:center;flex:none}
.step.left .ic{margin-right:16px}
.step.right{flex-direction:row-reverse}
.step.right .ic{margin-left:16px}
.step.right .txt{padding-left:24px}
.hub{top:300px;left:518px;width:162px;height:162px;border-radius:50%;background:#2a2a2a;border:10px solid rgba(255,255,255,.15)}

/* about */
.about{top:1676px;height:460px}
.portrait-frame{top:118px;left:202px;width:258px;height:272px;background:var(--sky);border-radius:0 0 0 12px}
.portrait{top:101px;left:191px;width:263px;height:274px;background:linear-gradient(160deg,#cfd6dc,#9fb2c4 55%,#5d86b8);border-radius:0 0 0 14px}
.about h3{top:103px;left:531px;font-family:"Roboto",sans-serif;font-weight:500;font-size:31px;color:var(--ink);letter-spacing:-.5px}
.about h3 em{font-style:normal;color:var(--sky)}
.about .cred{top:152px;left:531px;font-family:"Roboto",sans-serif;font-size:17px;color:var(--ink)}
.about p{top:196px;left:531px;width:480px;font-size:15.5px;line-height:27.5px;color:#333}
.about .btn{top:356px;left:531px;width:166px;background:var(--blue);height:44px}

/* get started */
.start{top:2136px;height:624px}
.start h2{position:absolute;top:38px;width:100%}
.pill{position:absolute;width:308px;height:112px;border:2px solid var(--sky);border-radius:56px;display:flex;align-items:center;padding-left:8px;background:var(--white);overflow:hidden}
.pill .ic{width:92px;height:92px;border-radius:50%;background:var(--blue);display:flex;align-items:center;justify-content:center;flex:none;border:5px solid #dbeaf5}
.pill .txt{padding-left:14px;padding-right:16px;min-width:0}
.pill h4{font-family:"Roboto",sans-serif;font-weight:500;font-size:17px;color:var(--ink);margin-bottom:5px}
.pill p{font-size:12px;line-height:18px;color:#333;letter-spacing:-.2px;white-space:nowrap}
.sq{width:36px;height:36px}

/* services */
.services{top:2763px;height:567px;background:var(--blue)}
.services h2{position:absolute;top:56px;width:100%;color:var(--white)}
.grid{position:absolute;top:149px;left:130px;display:grid;grid-template-columns:repeat(5,182px);grid-auto-rows:152px;gap:10px}
.tile{background:var(--tile);display:flex;flex-direction:column;align-items:center;justify-content:flex-end;padding-bottom:26px;gap:16px;font-family:"Roboto",sans-serif;font-weight:500;font-size:14.5px;color:var(--ink)}
.tile.active{background:var(--sky);color:var(--white)}

/* blog */
.blog{top:3330px;height:601px}
.blog h2{position:absolute;top:56px;width:100%}
.post{position:absolute;top:142px;width:374px;height:364px;background:var(--tile)}
.post .img{height:220px}
.post h4{margin:30px 26px 0;font-size:13.5px;font-weight:600;line-height:22px;color:var(--ink)}
.post p{margin:12px 26px 0;font-size:13.5px;line-height:22px;color:#333}
.post .go{position:absolute;right:28px;bottom:20px;width:22px;height:22px;border-radius:50%;background:var(--white);display:flex;align-items:center;justify-content:center}

/* testimonials */
.testimonials{top:3931px;height:548px;background:var(--blue)}
.testimonials h2{position:absolute;top:62px;width:100%;color:var(--white)}
.quote{position:absolute;top:146px;width:274px;height:170px;background:var(--white);text-align:center;padding-top:20px}
.quote::after{content:"";position:absolute;left:125px;bottom:-12px;border-left:12px solid transparent;border-right:12px solid transparent;border-top:12px solid var(--white)}
.stars{color:var(--star);font-size:16px;letter-spacing:2px}
.quote h5{font-size:13px;font-weight:500;color:var(--ink);margin:12px 0 10px}
.quote p{font-size:12px;line-height:21px;color:#777;padding:0 30px}
.person{position:absolute;top:340px;width:274px;text-align:center;color:var(--white)}
.avatar{width:58px;height:58px;border-radius:50%;background:#c9d3dd;border:3px solid var(--white);margin:0 auto 6px}
.person b{display:block;font-family:"Roboto",sans-serif;font-weight:500;font-size:15px}
.person span{font-size:13px}
.dots{top:468px;left:566px;display:flex;gap:6px;align-items:center}
.dots i{width:10px;height:10px;border-radius:50%;border:1.5px solid var(--white)}
.dots i.on{background:var(--white);width:12px;height:12px}

/* footer */
.site-footer{top:4479px;height:387px;background:var(--foot)}
.foot-brand{top:86px;left:121px;display:flex;align-items:center;gap:12px}
.foot-brand .brand-name{color:var(--sky);font-size:22px}
.foot-brand .brand-dot{background:#e5e5e5;width:42px;height:42px}
.social{top:180px;left:165px;display:flex;gap:22px}
.social i{width:16px;height:16px;border-radius:50%;background:var(--white);display:block}
.foot-links{top:48px;left:418px;list-style:none;font-size:12.5px;line-height:27px;color:var(--white)}
.field{position:absolute;background:var(--field);border:1px solid #4a4a50;font-size:13px;color:#999;padding:8px 14px}
.send{top:251px;left:567px;width:102px;height:36px;background:var(--blue);font-size:17px;border-radius:0}
.legal{position:absolute;top:321px;left:0;width:1200px;height:66px;background:var(--foot-deep);color:var(--white);font-size:12.5px}
.legal .copy{position:absolute;left:142px;top:24px}
.legal .terms{position:absolute;right:120px;top:24px;font-size:11.5px}
</style>
</head>
<body>

<header class="site-header">
  <div class="brand"><span class="brand-dot"></span><span class="brand-name">The Marlow<br>Wellness Studio</span></div>
  <div class="phone">
    <svg width="20" height="20" viewBox="0 0 24 24" fill="none" stroke="#3277b5" stroke-width="2"><path d="M5 3h4l2 5-2.5 1.5a11 11 0 0 0 6 6L16 13l5 2v4a2 2 0 0 1-2 2A17 17 0 0 1 3 5a2 2 0 0 1 2-2z"/></svg>
    555.010.0142
  </div>
  <nav class="nav"><span>Our Process</span><span>About</span><span>Services</span><span>Why Energy</span><span>Testimonials</span><span>Blog</span><span>Contact</span></nav>
</header>

<section class="hero" role="img" aria-label="Woman with arms raised on a mountain top above a misty valley">
  <div class="abs hero-title">Recharge Your Energy</div>
  <div class="abs hero-sub">for exceptional health and<br>performance</div>
  <div class="abs hero-btns">
    <span class="btn">Getting Srarted</span>
    <span class="btn btn-play"><span class="ic"><svg width="12" height="12" viewBox="0 0 12 12"><path d="M3 1l8 5-8 5z" fill="#3277b5"/></svg></span>Watch Video</span>
  </div>
</section>

<section class="why">
  <span class="abs ring" style="left:148px;top:90px;width:30px;height:30px"></span>
  <span class="abs ring" style="left:144px;top:180px;width:30px;height:30px"></span>
  <span class="abs ring" style="left:250px;top:150px;width:16px;height:16px"></span>
  <span class="abs ring" style="left:990px;top:78px;width:56px;height:56px"></span>
  <span class="abs ring" style="left:1018px;top:150px;width:42px;height:42px"></span>
  <span class="abs ring" style="left:1098px;top:60px;width:18px;height:18px"></span>
  <h2>Why do you feel the way you do</h2>
  <p>Lorem Ipsum is simply dummy text of the printing and typesetting industry. Lorem Ipsum has been the industry's standard dummy text ever since the 1500s, when an unknown printer took a galley of type and scrambled it to make a type specimen book.</p>
</section>

<section class="process" role="img" aria-label="Woman breathing in the sunset on a green hillside, arms open">
  <h2>Our Process</h2>
  <span class="abs rule"></span>
  <div class="step left" style="left:121px;top:232px">
    <div class="txt"><h3>Detect</h3><p>Use our body field scanner, at home to uncover why yhou feelthe way you do</p></div>
    <div class="ic"><svg width="44" height="44" viewBox="0 0 24 24" fill="none" stroke="#fff" stroke-width="2"><circle cx="14" cy="10" r="6"/><path d="M10 14l-7 7"/></svg></div>
  </div>
  <div class="step left" style="left:121px;top:397px">
    <div class="txt"><h3>Direct</h3><p>Use our body field scanner, at home to uncover why yhou feelthe way you do</p></div>
    <div class="ic"><svg width="44" height="44" viewBox="0 0 24 24" fill="none" stroke="#fff" stroke-width="2"><circle cx="5" cy="5" r="2"/><circle cx="19" cy="19" r="2"/><path d="M7 5h10a3 3 0 0 1 0 6H7a3 3 0 0 0 0 6h10"/></svg></div>
  </div>
  <div class="step right" style="left:697px;top:232px">
    <div class="txt"><h3>Correct</h3><p>Use our body field scanner, at home to uncover why yhou feelthe way you do</p></div>
    <div class="ic"><svg width="44" height="44" viewBox="0 0 24 24" fill="none" stroke="#fff" stroke-width="2.4"><circle cx="12" cy="12" r="9"/><path d="M7.5 12l3 3 6-6"/></svg></div>
  </div>
  <div class="step right" style="left:697px;top:397px">
    <div class="txt"><h3>Re-Connect</h3><p>Use our body field scanner, at home to uncover why yhou feelthe way you do</p></div>
    <div class="ic"><svg width="44" height="44" viewBox="0 0 24 24" fill="none" stroke="#fff" stroke-width="3"><path d="M19 12a7 7 0 1 1-2-5"/><path d="M18 3v5h-5"/></svg></div>
  </div>
  <span class="abs hub"></span>
</section>

<section class="about">
  <span class="abs portrait-frame"></span>
  <div class="abs portrait" role="img" aria-label="Portrait of practitioner Tobin R Hartwell seated at home"></div>
  <h3 class="abs">About <em>Tobin R Hartwell</em></h3>
  <div class="abs cred">FDN-P HPCPFCPBC</div>
  <p class="abs">Lorem Ipsum is simply dummy text of the printing and typesetting industry. Lorem Ipsum has been the industry's standard dummy text ever since the 1500s, when an unknown printer took a galley of type and scrambled it to make a type specimen book.</p>
  <span class="abs btn">Read More</span>
</section>

<section class="start">
  <h2>How to <em>Get Started</em></h2>
  <div class="pill" style="left:278px;top:137px"><span class="ic"><svg width="40" height="40" viewBox="0 0 24 24" fill="none" stroke="#fff" stroke-width="1.8"><rect x="5" y="3" width="14" height="18" rx="2"/><path d="M8 8h8M8 12h8M8 16h4"/></svg></span><div class="txt"><h4>Register</h4><p>Get your lifetime access<br>@marlowstudio.example/Vireq</p></div></div>
  <div class="pill" style="left:614px;top:137px"><span class="ic"><svg width="40" height="40" viewBox="0 0 24 24" fill="none" stroke="#fff" stroke-width="1.8"><rect x="6" y="2" width="12" height="20" rx="2"/><path d="M9 9h6v6H9z"/></svg></span><div class="txt"><h4>Get Scanner</h4><p>Buy a scanner<br>portal.vireqhealth.example</p></div></div>
  <div class="pill" style="left:113px;top:275px"><span class="ic"><svg width="40" height="40" viewBox="0 0 24 24" fill="none" stroke="#fff" stroke-width="2"><path d="M12 3v11M7 10l5 5 5-5M4 19h16"/></svg></span><div class="txt"><h4>Download</h4><p>Download the smart<br>phone app vitalpath</p></div></div>
  <div class="pill" style="left:446px;top:275px"><span class="ic"><svg width="40" height="40" viewBox="0 0 24 24" fill="none" stroke="#fff" stroke-width="1.8"><circle cx="12" cy="12" r="8"/><circle cx="12" cy="12" r="3"/></svg></span><div class="txt"><h4>Detect</h4><p>Pair your scanner with<br>the app &amp; scan</p></div></div>
  <div class="pill" style="left:779px;top:275px"><span class="ic"><svg width="40" height="40" viewBox="0 0 24 24" fill="none" stroke="#fff" stroke-width="2"><circle cx="5" cy="5" r="2"/><circle cx="19" cy="19" r="2"/><path d="M7 5h10a3 3 0 0 1 0 6H7a3 3 0 0 0 0 6h10"/></svg></span><div class="txt"><h4>Direct</h4><p>Follow simple guidelines<br>&amp; improve energy</p></div></div>
  <div class="pill" style="left:278px;top:411px"><span class="ic"><svg width="40" height="40" viewBox="0 0 24 24" fill="none" stroke="#fff" stroke-width="2.2"><circle cx="12" cy="12" r="9"/><path d="M7.5 12l3 3 6-6"/></svg></span><div class="txt"><h4>Correct</h4><p>Buy "Feel Good"<br>Vitaltones</p></div></div>
  <div class="pill" style="left:614px;top:411px"><span class="ic"><svg width="40" height="40" viewBox="0 0 24 24" fill="none" stroke="#fff" stroke-width="2"><rect x="3" y="8" width="11" height="8" rx="4"/><rect x="10" y="8" width="11" height="8" rx="4"/></svg></span><div class="txt"><h4>Reconnect</h4><p>Follow guidelines for<br>sustainable results</p></div></div>
  <span class="abs sq" style="left:1058px;top:494px;background:var(--sky)"></span>
  <span class="abs sq" style="left:1106px;top:494px;background:var(--blue)"></span>
</section>

<section class="services">
  <h2>Our Services</h2>
  <div class="grid">
    <div class="tile active"><svg width="52" height="52" viewBox="0 0 48 48" fill="none" stroke="#fff" stroke-width="1.6"><circle cx="24" cy="18" r="9"/><path d="M20 27v5h8v-5M6 28l10 12h16l10-12"/></svg>Energy Source</div>
    <div class="tile"><svg width="52" height="52" viewBox="0 0 48 48" fill="none" stroke="#333" stroke-width="1.6"><path d="M24 6l8 5v9l-8 5-8-5v-9zM16 20l8 5v9l-8 5-8-5v-9zM32 20l8 5v9l-8 5-8-5"/></svg>Energetic Drivers</div>
    <div class="tile"><svg width="52" height="52" viewBox="0 0 48 48" fill="none" stroke="#333" stroke-width="1.6"><path d="M4 14c7-6 13 6 20 0s13 6 20 0M4 24c7-6 13 6 20 0s13 6 20 0M4 34c7-6 13 6 20 0s13 6 20 0"/></svg>Energetic Flow</div>
    <div class="tile"><svg width="52" height="52" viewBox="0 0 48 48" fill="none" stroke="#333" stroke-width="1.6"><path d="M14 42v-8c-5-3-7-8-6-14C10 10 18 5 27 6c9 1 14 8 13 16l4 6-4 1v6h-8v7"/></svg>Mind Body</div>
    <div class="tile"><svg width="52" height="52" viewBox="0 0 48 48" fill="none" stroke="#333" stroke-width="1.6"><circle cx="18" cy="16" r="10"/><path d="M18 26v16M6 42h36M30 42V28h8v14"/></svg>Energetic Terrians</div>
    <div class="tile"><svg width="52" height="52" viewBox="0 0 48 48" fill="none" stroke="#333" stroke-width="1.6"><path d="M22 4l5 12 13 1-10 8 3 13-11-7-11 7 3-13-10-8 13-1z"/><path d="M33 30l2 5 5 .5-4 3 1.5 5-4.5-3-4.5 3 1.5-5-4-3 5-.5z" fill="#333"/></svg>Energetic Stars</div>
    <div class="tile"><svg width="52" height="52" viewBox="0 0 48 48" fill="none" stroke="#333" stroke-width="1.6"><rect x="14" y="4" width="20" height="40" rx="3"/><circle cx="24" cy="36" r="2"/><path d="M18 10h12v18H18z"/></svg>Energetic Rejuvenators</div>
    <div class="tile"><svg width="52" height="52" viewBox="0 0 48 48" fill="none" stroke="#333" stroke-width="1.6"><path d="M24 28V14M24 18c0-6 6-9 12-8-1 6-6 9-12 8M24 22c0-5-5-7-10-6 1 5 5 7 10 6M4 32c8 0 12 6 20 6s12-4 20-8"/></svg>Environment</div>
    <div class="tile"><svg width="52" height="52" viewBox="0 0 48 48" fill="none" stroke="#333" stroke-width="1.6"><rect x="10" y="16" width="14" height="26" rx="3"/><path d="M13 16V8h8v8"/><circle cx="33" cy="32" r="9"/><path d="M33 23c0-4 3-6 6-6"/></svg>Nutrition</div>
    <div class="tile"><svg width="52" height="52" viewBox="0 0 48 48" fill="none" stroke="#333" stroke-width="1.6"><rect x="10" y="6" width="28" height="36" rx="2"/><path d="M15 16h4v4h-4zM15 26h4v4h-4zM23 18h10M23 28h10M15 36h18"/></svg>Recommendations</div>
  </div>
</section>

<section class="blog">
  <h2>Our <em>Blog</em></h2>
  <article class="post" style="left:214px">
    <div class="img" role="img" aria-label="Woman with backpack raising her arms over a green valley" style="background:linear-gradient(180deg,#b9c9cf,#7f8f76 55%,#5f6a4b)"></div>
    <h4>Lorem Ipsum is simply dummy text of the printingindustry</h4>
    <p>Lorem Ipsum is simply dummy text of the printing typesetting industry.</p>
    <span class="go"><svg width="8" height="8" viewBox="0 0 8 8"><path d="M2 1l3 3-3 3" stroke="#3277b5" fill="none" stroke-width="1.4"/></svg></span>
  </article>
  <article class="post" style="left:612px">
    <div class="img" role="img" aria-label="Person holding an umbrella with arms open in misty hills" style="background:linear-gradient(180deg,#d9dddd,#a9b3ac 55%,#56644c)"></div>
    <h4>Lorem Ipsum is simply dummy text of the printingindustry</h4>
    <p>Lorem Ipsum is simply dummy text of the printing typesetting industry.</p>
    <span class="go"><svg width="8" height="8" viewBox="0 0 8 8"><path d="M2 1l3 3-3 3" stroke="#3277b5" fill="none" stroke-width="1.4"/></svg></span>
  </article>
</section>

<section class="testimonials">
  <h2>Client Testimonials</h2>
  <div class="quote" style="left:163px"><div class="stars">★★★★★</div><h5>"Solid Service! Vety consitent!"</h5><p>the printing and typesetting industry. Lorem Ipsum has been the industry's standard dummy</p></div>
  <div class="quote" style="left:461px"><div class="stars">★★★★★</div><h5>"Solid Service! Vety consitent!"</h5><p>the printing and typesetting industry. Lorem Ipsum has been the industry's standard dummy</p></div>
  <div class="quote" style="left:762px"><div class="stars">★★★★★</div><h5>"Solid Service! Vety consitent!"</h5><p>the printing and typesetting industry. Lorem Ipsum has been the industry's standard dummy</p></div>
  <div class="person" style="left:163px"><div class="avatar" role="img" aria-label="Client photo"></div><b>Clara Denholm</b><span>Web Development</span></div>
  <div class="person" style="left:461px"><div class="avatar" role="img" aria-label="Client photo"></div><b>Clara Denholm</b><span>Web Development</span></div>
  <div class="person" style="left:762px"><div class="avatar" role="img" aria-label="Client photo"></div><b>Clara Denholm</b><span>Web Development</span></div>
  <div class="abs dots"><i></i><i class="on"></i><i></i><i></i></div>
</section>

<footer class="site-footer">
  <div class="abs foot-brand"><span class="brand-dot"></span><span class="brand-name">The Marlow<br>Wellness Studio</span></div>
  <div class="abs social" aria-label="Social links"><i></i><i></i><i></i></div>
  <ul class="abs foot-links"><li>Home</li><li>Our Process</li><li>Services</li><li>Why Energy</li><li>Testimonials</li><li>Blog</li><li>Contacts</li></ul>
  <div class="field" style="left:567px;top:48px;width:243px;height:38px">Name</div>
  <div class="field" style="left:834px;top:48px;width:243px;height:38px">Email</div>
  <div class="field" style="left:567px;top:95px;width:510px;height:34px">Subject</div>
  <div class="field" style="left:567px;top:138px;width:510px;height:95px">Message</div>
  <span class="abs btn send">Send</span>
  <div class="legal"><span class="copy">Copyright 2020 The Marlow Wellness Studio. All Rights Reserved.</span><span class="terms">Privacy Policy &nbsp;|&nbsp; Terms Of Services</span></div>
</footer>

</body>
</html>
```